Professional digital stationary

We need a digital stationary for our brand, we already have a logo and based on that we need a design for Word, Powerpoint, mailings and Linkedin. We need to be able to re use the stationary for other things like other social media. So basically what we ask is a template for Powerpoint and Word, some e-mail headers and a nice and professional Linkedin Header.

Target Market(s)

recruitment

Font styles to use
Sans Serif

```html
<!DOCTYPE html>
<html lang="en">
<head>
<meta charset="utf-8">
<title>tidewell – LinkedIn header</title>
<link href="https://fonts.googleapis.com/css2?family=Quicksand:wght@300;400&display=swap" rel="stylesheet">
<style>
  :root {
    --page: #ffffff;
    --band: #070706;
    --photo-dark: #0b0b0a;
    --photo-mid: #2a2820;
    --photo-gold: #8a7440;
    --brand-green: #9cc84b;
    --tagline: #f2f2f2;
  }
  html, body {
    margin: 0;
    padding: 0;
    width: 1200px;
    height: 1200px;
    overflow: hidden;
    background: var(--page);
  }
  .canvas {
    position: relative;
    width: 1200px;
    height: 1200px;
    background: var(--page);
  }
  .header-band {
    position: absolute;
    left: 120px;
    top: 442px;
    width: 960px;
    height: 317px;
    background: var(--band);
    overflow: hidden;
  }
  .hero-photo {
    position: absolute;
    left: 0;
    top: 36px;
    width: 348px;
    height: 281px;
    background:
      radial-gradient(ellipse 38% 30% at 55% 40%, var(--photo-gold) 0%, rgba(138,116,64,0.5) 45%, transparent 75%),
      radial-gradient(ellipse 60% 45% at 50% 62%, var(--photo-mid) 0%, transparent 80%),
      var(--photo-dark);
  }
  .brand-lockup {
    position: absolute;
    left: 470px;
    bottom: 52px;
    font-family: "Quicksand", sans-serif;
    white-space: nowrap;
  }
  .brand-name {
    margin: 0;
    font-weight: 300;
    font-size: 96px;
    line-height: 0.9;
    letter-spacing: -1px;
    color: var(--brand-green);
  }
  .brand-tagline {
    margin: 4px 0 0 3px;
    font-weight: 400;
    font-size: 21px;
    line-height: 1.2;
    color: var(--tagline);
  }
</style>
</head>
<body>
  <main class="canvas">
    <section class="header-band">
      <div class="hero-photo" role="img" aria-label="Three golden eggs resting in a nest of dry grass on a dark background"></div>
      <div class="brand-lockup">
        <h1 class="brand-name">tidewell</h1>
        <p class="brand-tagline">More value, more flexibility</p>
      </div>
    </section>
  </main>
</body>
</html>
```